Football and Sports Management Agency Stationary

We have a logo, fonts, website and colour palette.
We need the logo refined by a proper designer and then business stationary designed. You can see on the website how it needs adjusting by a designers eye.
The company is a high end sports management company aiming to attract and represent professional athletes. The name Velorin is to indicate a 'Constellation of Stars' ie our clients. The dots on the star should be slightly different sizes to reflect that some clients will be bigger than others.
Colours:
#e6e6e6
#edd2a4
#caaa72 (main gold and also used on site)
#3f3f42
#001d38
#edeced (on website)
#191c23 (on website)
Font:
QT (velorin)
QT Melbrook (sports management)
We would like:
- Letterhead (word and indesign and PDF print format). I have attached an example for one I like. It's quiet a clean design with the contact details and address taking up only a small amount of room.
- Business card (dark on the back with the logo, personal details on the front). Only needs name, title, email, website and phone number. No company address (in PDF and indesign format)
- Powerpoint slide theme
- Logo in vector format for light and dark versions and single colour versions. And optimised web version
- Simple brand guide PDF showing colour, font and logo (a one/two page PDF)
Any questions, please ask.
NEW INFO:
Contact Details
Maren Solwick
Director
Mobile: +44 7630 218 977
Phone: +44 0113 872 604
Email: maren@velorinathletic.example
Web: velorinathletic.example
Corran Lodge, 14 Mill Bank Road, Stockport, SK4 9TW
Company number 40718362
Target Market(s)
Professional athletes, professional sports teams.
Industry/Entity Type
Management
Requirements
Must have
- NEW
- The designs must look cool, classy and high quality. My suggestion for this is to keep the text small and precise with uncomplicated design.
Nice to have
- Application of brand displayed on stationary and additional pieces of stationary branded.
- Draw some inspiration from the website. eg the slant angles used separate the sections.
Should not have
- Don't create new logos etc.

```html
<!DOCTYPE html>
<html lang="en">
<head>
<meta charset="utf-8">
<title>Velorin – Business Card, Option 5</title>
<link href="https://fonts.googleapis.com/css2?family=Open+Sans:ital,wght@0,300;0,400;0,700;1,700&display=swap" rel="stylesheet">
<style>
  :root {
    --board: #e0e0e0;
    --navy: #0a1d36;
    --navy-ink: #0b1e36;
    --gold: #caaa72;
    --gold-light: #d8b97e;
    --white: #ffffff;
  }
  * { margin: 0; padding: 0; box-sizing: border-box; }
  html, body { width: 1200px; height: 1000px; overflow: hidden; }
  body {
    position: relative;
    background: var(--board);
    font-family: "Open Sans", Arial, sans-serif;
  }
  .option-title {
    position: absolute; left: 66px; top: 52px;
    font-size: 44px; font-weight: 700; font-style: italic;
    color: var(--navy-ink); letter-spacing: -0.5px;
  }
  .card {
    position: absolute; top: 329px; width: 511px; height: 343px;
    background: var(--navy);
    overflow: hidden;
  }
  .card--back { left: 67px; box-shadow: 0 4px 8px rgba(0,0,0,0.25); }
  .card--front { left: 623px; box-shadow: 0 18px 40px rgba(0,0,0,0.28); }

  .wordmark {
    position: absolute; left: 0; right: 0; top: 186px;
    text-align: center;
    font-weight: 300; font-size: 30px; letter-spacing: 12px; padding-left: 12px;
    color: var(--white);
  }
  .wordmark-dot {
    position: absolute; left: 250px; top: 150px;
    width: 12px; height: 12px; border-radius: 50%;
    background: var(--gold);
  }
  .front-name-mark {
    position: absolute; left: 60px; top: 157px; width: 142px;
    text-align: center;
    font-weight: 300; font-size: 20px; letter-spacing: 5px;
    color: var(--gold);
  }
  .holder {
    position: absolute; left: 260px; top: 100px; width: 232px;
  }
  .holder-name {
    font-size: 22px; font-weight: 700; line-height: 28px;
    color: var(--gold); text-transform: uppercase; white-space: nowrap;
  }
  .holder-role { font-size: 15px; color: var(--white); line-height: 18px; }
  .contact-list { list-style: none; margin-top: 14px; }
  .contact-list li {
    display: flex; align-items: center; height: 28px;
    font-size: 14px; color: var(--white); white-space: nowrap;
  }
  .contact-list svg { width: 12px; height: 12px; margin: 0 12px 0 0; flex: none; }

  .detail {
    position: absolute; left: 628px; top: 750px; width: 189px; height: 189px;
    background: var(--navy); overflow: hidden;
  }
  .detail-list { list-style: none; position: absolute; left: 73px; top: 16px; }
  .detail-list li {
    display: flex; align-items: center; height: 55px;
    font-size: 29px; color: var(--white); white-space: nowrap;
  }
  .detail-list svg { width: 25px; height: 25px; margin-right: 33px; flex: none; }
</style>
</head>
<body>
  <svg width="0" height="0" style="position:absolute" aria-hidden="true">
    <defs>
      <symbol id="icon-phone" viewBox="0 0 24 24">
        <circle cx="12" cy="12" r="12" fill="#caaa72"/>
        <path d="M8.2 5.8l2 2.6-1.2 1.4c.8 1.8 2.2 3.3 4.1 4.2l1.4-1.2 2.6 2-1.1 2.4c-4.6-.6-8.6-4.6-9.2-9.2z" fill="#0a1d36"/>
      </symbol>
      <symbol id="icon-mail" viewBox="0 0 24 24">
        <circle cx="12" cy="12" r="12" fill="#caaa72"/>
        <rect x="6" y="8" width="12" height="8.5" fill="#0a1d36"/>
        <path d="M6.5 8.5l5.5 4.3 5.5-4.3" fill="none" stroke="#caaa72" stroke-width="1"/>
      </symbol>
      <symbol id="icon-globe" viewBox="0 0 24 24">
        <circle cx="12" cy="12" r="12" fill="#caaa72"/>
        <g fill="none" stroke="#0a1d36" stroke-width="1">
          <circle cx="12" cy="12" r="6.5"/>
          <ellipse cx="12" cy="12" rx="3" ry="6.5"/>
          <path d="M12 5.5v13M5.5 12h13M6.5 8.8h11M6.5 15.2h11"/>
        </g>
      </symbol>
    </defs>
  </svg>

  <h1 class="option-title">Option 5</h1>

  <section class="card card--back" aria-label="Card back">
    <span class="wordmark-dot"></span>
    <div class="wordmark">VELORIN</div>
  </section>

  <section class="card card--front" aria-label="Card front">
    <div class="front-name-mark">VELORIN</div>
    <div class="holder">
      <div class="holder-name">Maren Solwick</div>
      <div class="holder-role">Director</div>
      <ul class="contact-list">
        <li><svg><use href="#icon-phone"/></svg>+44 0113 872 604</li>
        <li><svg><use href="#icon-mail"/></svg>velorinathletic.example</li>
        <li><svg><use href="#icon-globe"/></svg>maren@velorinathletic.example</li>
      </ul>
    </div>
  </section>

  <section class="detail" aria-label="Contact detail close-up">
    <ul class="detail-list">
      <li><svg><use href="#icon-phone"/></svg>+44 0113 872 604</li>
      <li><svg><use href="#icon-mail"/></svg>velorinathletic.example</li>
      <li><svg><use href="#icon-globe"/></svg>maren@velorinathletic.example</li>
    </ul>
  </section>
</body>
</html>
```